Business Card

I need a business card that really pops for a potential customer or person who refers a personal injury lead. I want to highlight our office locations, but only address that needs to be on the card is my office's main address. I want a sleek, modern and minimalist design.

```html
<!DOCTYPE html>
<html lang="en">
<head>
<meta charset="utf-8">
<title>Northfield Injury Lawyers — Business Card</title>
<link rel="stylesheet" href="https://fonts.googleapis.com/css2?family=Open+Sans:wght@400;700&display=swap">
<style>
  :root {
    --backdrop: #222222;
    --card: #3a3a3a;
    --card-edge: #2c2c2c;
    --mark: #2b2b2b;
    --ink: #ffffff;
    --ink-soft: #e6e6e6;
  }
  * { box-sizing: border-box; margin: 0; padding: 0; }
  html, body {
    width: 1200px; height: 780px; overflow: hidden;
    background: var(--backdrop);
  }
  .canvas {
    width: 1200px; height: 780px;
    display: flex; align-items: center; justify-content: center; gap: 40px;
  }
  .card {
    position: relative;
    width: 540px; height: 309px;
    background: var(--card);
    box-shadow: 0 2px 0 var(--card-edge), 0 14px 30px rgba(0,0,0,.45);
    overflow: hidden;
  }

  /* placeholder firm name, plain text */
  .firm-name {
    font-family: "Open Sans", sans-serif;
    font-weight: 400;
    color: var(--mark);
    white-space: nowrap;
    display: flex; align-items: center; gap: 10px;
  }
  .firm-name .firm-dot {
    display: inline-block; width: 10px; height: 10px; background: var(--mark);
  }

  /* contact side */
  .card--contact .firm-name {
    position: absolute; left: 26px; top: 50%;
    writing-mode: vertical-rl;
    transform: translateY(-50%);
    font-size: 16px;
  }
  .contact {
    position: absolute; right: 34px; bottom: 26px;
    text-align: right;
    font-family: "Open Sans", sans-serif; color: var(--ink-soft);
  }
  .contact .person { font-size: 28px; font-weight: 700; color: var(--ink); line-height: 1.05; }
  .contact .role { font-size: 13px; color: var(--ink); margin-bottom: 10px; }
  .contact .address { font-size: 12.5px; line-height: 1.4; margin-bottom: 8px; }
  .contact .line {
    display: flex; justify-content: flex-end; align-items: center; gap: 7px;
    font-size: 12.5px; line-height: 1.55;
  }
  .contact .line svg { width: 12px; height: 12px; fill: var(--ink); }
  .accent-tab {
    position: absolute; right: 0; top: 124px;
    width: 16px; height: 46px; background: var(--ink);
  }

  /* brand side */
  .card--mark .firm-name {
    position: absolute; left: 60px; top: 50%;
    transform: translateY(-50%);
    font-size: 34px;
  }
  .card--mark .firm-dot { width: 16px; height: 16px; }
</style>
</head>
<body>
<main class="canvas">
  <section class="card card--contact" aria-label="Business card, contact side">
    <p class="firm-name">Northfield Injury Lawyers</p>
    <div class="accent-tab"></div>
    <div class="contact">
      <p class="person">Dalton Reeves</p>
      <p class="role">Lawyers</p>
      <p class="address">480 W. Harbor Street, Suite 2100,<br>Lakemont, IL, United States, Illinois</p>
      <p class="line">+1 555-014-2290
        <svg viewBox="0 0 24 24" aria-hidden="true"><path d="M6.6 10.8a15.5 15.5 0 0 0 6.6 6.6l2.2-2.2a1 1 0 0 1 1-.25 11.4 11.4 0 0 0 3.6.57 1 1 0 0 1 1 1V20a1 1 0 0 1-1 1A17 17 0 0 1 3 4a1 1 0 0 1 1-1h3.5a1 1 0 0 1 1 1c0 1.25.2 2.45.57 3.57a1 1 0 0 1-.25 1z"/></svg>
      </p>
      <p class="line">info@northfieldinjurylaw.com
        <svg viewBox="0 0 24 24" aria-hidden="true"><path d="M2 5h20v14H2zm2 2v.5l8 5 8-5V7zm0 2.8V17h16V9.8l-8 5z"/></svg>
      </p>
      <p class="line">www.northfieldinjurylaw.com
        <svg viewBox="0 0 24 24" aria-hidden="true"><path d="M12 2a10 10 0 1 0 0 20 10 10 0 0 0 0-20zm6.9 6h-3a15 15 0 0 0-1.3-3.9A8 8 0 0 1 18.9 8zM12 4c.8 1.1 1.5 2.5 1.9 4h-3.8c.4-1.5 1.1-2.9 1.9-4zM4.3 14a8 8 0 0 1 0-4h3.4a16 16 0 0 0 0 4zm.8 2h3a15 15 0 0 0 1.3 3.9A8 8 0 0 1 5.1 16zm3-8h-3a8 8 0 0 1 4.3-3.9A15 15 0 0 0 8.1 8zM12 20c-.8-1.1-1.5-2.5-1.9-4h3.8c-.4 1.5-1.1 2.9-1.9 4zm2.3-6H9.7a14 14 0 0 1 0-4h4.6a14 14 0 0 1 0 4zm.3 5.9a15 15 0 0 0 1.3-3.9h3a8 8 0 0 1-4.3 3.9zm1.7-5.9a16 16 0 0 0 0-4h3.4a8 8 0 0 1 0 4z"/></svg>
      </p>
    </div>
  </section>

  <section class="card card--mark" aria-label="Business card, brand side">
    <p class="firm-name"><span class="firm-dot"></span>Northfield Injury Lawyers</p>
  </section>
</main>
</body>
</html>
```